Cat-products company needs smart, yet endearing, business card

We need a business card design for a new, but up-and-running, business based in Honolulu, Hawaii. The business is Purrlane Nest Co. Our first product is the most environmentally-friendly cat grass kit ever seen on the planet. Future products, currently in the R&D phase, will include a variety of exciting cat scratchers. We also do consulting work to help apartment-dwellers make their home more cat-friendly and, in the future, plan on doing full, custom installs of structure to create high walkways for cats.

Target Market(s)

Middle-aged, apartment-dwelling, middle-class workers who own 1 or more cats and who dote on them.

Industry/Entity Type

Pet Care

Contact Information for Business Card

A striking, professional, yet warm and friendly design is what we're after.

Font styles to use
Serif
Sans Serif
Other font styles liked:
• Comfortaa

Colors

Designer to choose colors to be used in the design.

Requirements
Must have
• The company logo: (see attachment)
• The company name: Purrlane Nest Co
• The web address: www.purrlanenestco.example
• Email: support@purrlanenestco.example
• Phone: +1 (808) 555 0172
• Update (Fri Jun 30 3017 7:45pm Hawaii Time) I would like, is possible, uploaded picture of the cat grass kit on the back of the card with some text along the lines of: Purrlane Nest Co - Where The Freshest Kitty Sprouts Begin
Nice to have
• A cat picture, cartoon, real or silhouette that illustrates cats in action and/or relaxing; ie using the apartment space to live, play and relax in and being well-contented.
• Most of the website is done in the font: Comfortaa. It might be nice to continue using this for brand consistency.
Should not have
• Hard-to-read fonts.

```html
<!DOCTYPE html>
<html lang="en">
<head>
<meta charset="utf-8">
<title>Purrlane Nest Co – Business Card</title>
<link href="https://fonts.googleapis.com/css2?family=Comfortaa:wght@700&family=Open+Sans:wght@400;600&display=swap" rel="stylesheet">
<style>
  :root {
    --bg: #ece8e2;
    --green: #b6d22f;
    --green-light: #eaf7a8;
    --green-mid: #c6e06a;
    --brown: #7b4334;
    --ink: #4a4a4a;
    --card-white: #ffffff;
    --card-grey: #e4e4e4;
    --photo-warm: #e9a25a;
    --photo-neutral: #d9d2c8;
    --social: #b7b7b7;
  }
  * { margin: 0; padding: 0; box-sizing: border-box; }
  html, body { width: 1200px; height: 1023px; overflow: hidden; }
  body {
    background: var(--bg);
    display: flex;
    flex-direction: column;
    align-items: center;
    justify-content: center;
    gap: 56px;
    font-family: "Open Sans", Arial, sans-serif;
  }
  .card {
    width: 700px;
    height: 400px;
    border-radius: 22px;
    position: relative;
    overflow: hidden;
    box-shadow: 0 6px 18px rgba(0,0,0,0.18);
  }

  /* Front */
  .card-front {
    background: radial-gradient(ellipse at 60% 40%, var(--green-light) 0%, var(--green-mid) 80%, #a9cb4a 100%);
    display: flex;
    align-items: center;
    justify-content: center;
  }
  .brand {
    display: flex;
    align-items: center;
    gap: 26px;
  }
  .brand-mark {
    width: 96px;
    height: 96px;
    background: var(--brown);
    border-radius: 6px;
  }
  .brand-name {
    font-family: "Comfortaa", "Trebuchet MS", sans-serif;
    font-weight: 700;
    color: var(--brown);
    font-size: 56px;
    line-height: 1;
    letter-spacing: -0.5px;
  }

  /* Back */
  .card-back {
    background: linear-gradient(135deg, var(--card-white) 0%, #f3f3f3 55%, var(--card-grey) 100%);
  }
  .back-brand {
    position: absolute;
    left: 48px;
    top: 40px;
    display: flex;
    align-items: center;
    gap: 12px;
  }
  .back-brand .brand-mark { width: 38px; height: 38px; border-radius: 4px; }
  .back-brand .brand-name { font-size: 24px; }
  .person {
    position: absolute;
    left: 48px;
    top: 112px;
  }
  .person-name {
    font-family: "Comfortaa", "Trebuchet MS", sans-serif;
    font-weight: 700;
    color: var(--green);
    font-size: 30px;
    letter-spacing: 1.5px;
  }
  .person-title {
    font-family: "Comfortaa", "Trebuchet MS", sans-serif;
    font-weight: 700;
    color: var(--brown);
    font-size: 16px;
    margin-top: 8px;
    letter-spacing: 1px;
  }
  .contacts {
    position: absolute;
    left: 48px;
    top: 218px;
    list-style: none;
    display: flex;
    flex-direction: column;
    gap: 12px;
  }
  .contacts li {
    display: flex;
    align-items: center;
    gap: 12px;
    font-size: 15px;
    color: var(--ink);
    letter-spacing: 0.6px;
  }
  .contact-icon {
    width: 22px;
    height: 22px;
    border-radius: 4px;
    display: flex;
    align-items: center;
    justify-content: center;
  }
  .icon-green { background: var(--green); }
  .icon-brown { background: var(--brown); }
  .socials {
    position: absolute;
    right: 30px;
    top: 30px;
    display: flex;
    gap: 12px;
  }
  .social-dot {
    width: 16px;
    height: 16px;
    border-radius: 50%;
    background: var(--social);
  }
  .cat-photo {
    position: absolute;
    right: 40px;
    bottom: 28px;
    width: 270px;
    height: 290px;
    border-radius: 14px;
    background: radial-gradient(ellipse at 55% 45%, var(--photo-neutral) 0%, #efe9e1 55%, rgba(243,243,243,0) 75%),
                radial-gradient(circle at 25% 80%, var(--photo-warm) 0%, rgba(233,162,90,0) 35%);
  }
</style>
</head>
<body>
  <section class="card card-front">
    <div class="brand">
      <span class="brand-mark"></span>
      <span class="brand-name">Purrlane Nest Co</span>
    </div>
  </section>

  <section class="card card-back">
    <div class="back-brand">
      <span class="brand-mark"></span>
      <span class="brand-name">Purrlane Nest Co</span>
    </div>

    <div class="person">
      <p class="person-name">Your Name</p>
      <p class="person-title">Title</p>
    </div>

    <ul class="contacts">
      <li>
        <span class="contact-icon icon-green">
          <svg width="14" height="14" viewBox="0 0 24 24"><path d="M6.6 10.8a15 15 0 0 0 6.6 6.6l2.2-2.2c.3-.3.7-.4 1-.2 1.1.4 2.3.6 3.6.6.6 0 1 .4 1 1V20c0 .6-.4 1-1 1A17 17 0 0 1 3 4c0-.6.4-1 1-1h3.5c.6 0 1 .4 1 1 0 1.3.2 2.5.6 3.6.1.3 0 .7-.2 1z" fill="#fff"/></svg>
        </span>
        +1 (808) 555 0172
      </li>
      <li>
        <span class="contact-icon icon-brown">
          <svg width="14" height="14" viewBox="0 0 24 24"><rect x="3" y="6" width="18" height="12" rx="1.5" fill="none" stroke="#fff" stroke-width="2"/><path d="M3 7l9 6 9-6" fill="none" stroke="#fff" stroke-width="2"/></svg>
        </span>
        support@purrlanenestco.example
      </li>
      <li>
        <span class="contact-icon icon-green">
          <svg width="14" height="14" viewBox="0 0 24 24"><circle cx="12" cy="12" r="9" fill="none" stroke="#fff" stroke-width="2"/><path d="M3 12h18M12 3c3 3 3 15 0 18M12 3c-3 3-3 15 0 18" fill="none" stroke="#fff" stroke-width="1.6"/></svg>
        </span>
        www.purrlanenestco.example
      </li>
    </ul>

    <div class="socials" aria-hidden="true">
      <span class="social-dot"></span>
      <span class="social-dot"></span>
      <span class="social-dot"></span>
      <span class="social-dot"></span>
    </div>

    <div class="cat-photo" role="img" aria-label="Photo of a playful cat on its back batting at orange balls of yarn"></div>
  </section>
</body>
</html>
```